QBrook718 Business Card Design

I am in need of a business card design.

Business Name: Harbor Stone 718 or Qbrook718 (we can try the business card with both variations)

I would like it to be somewhat different from the "average" business card

What do we do?

We link up with distributors of different items and we Market their products, sell their products, fulfill the shipment, and handle all customer service that goes along with it.

I will be uploading our logo as well as other business card ideas that i have seen and liked on the web.

I like the style of the "graphic design" business card that i uploaded. I was thinking maybe something like that but instead would read.

SYNC | SELL | SHIP

With maybe:
a computer or a Sync icon underneath SYNC
Some form of money sign underneath Sell
a delivery truck or something underneath SHIP.

And then I was thinking maybe put the logo on the back side like in the other business card that i uploaded.

I definitely want a double sided business card.

These are only my suggestions and if i was very confident in my idea then I wouldn't have to be on here. (So make what you think is nice because my opinion is probably not so great anyway!!)

Everything can be changed.

ALSO, For the logo
We can try and remove the text multi channel selling

For the Business card contact info:
Tom Haskins
CEO
2419 Pelkey Avenue
J7R-2B8
Montreal, Quebec

Thanks

Target Market(s)

Businesses

Industry/Entity Type

Information Technology

Font styles to use
Serif
Sans Serif
Decorative

Colors
34a6d6
33b8a4
aaaaaa
85cae6
33a6d7
0492cd
9d9d9d

Requirements
Must have
• Double Sided Business card
Nice to have
• Illustration graphics / Icons underneath the main points

```html
<!DOCTYPE html>
<html lang="en">
<head>
<meta charset="utf-8">
<title>Qbrook718 Business Card</title>
<link href="https://fonts.googleapis.com/css2?family=Open+Sans:ital,wght@0,300;0,700;1,400&family=Bebas+Neue&family=Jura:wght@400&display=swap" rel="stylesheet">
<style>
  :root {
    --backdrop: #a6ecef;
    --card: #ffffff;
    --band-light: #93eff2;
    --band-strong: #00fdfd;
    --ink: #111111;
    --brand-grey: #626262;
    --brand-blue: #39aef0;
    --tagline: #6f7f84;
    --icon: #686868;
  }
  html, body {
    margin: 0;
    width: 1200px;
    height: 1200px;
    overflow: hidden;
    background: var(--backdrop);
  }
  .canvas { position: relative; width: 1200px; height: 1200px; }
  .card {
    position: absolute;
    background: var(--card);
    border-radius: 34px;
    overflow: hidden;
  }
  .card-front { left: 165px; top: 59px; width: 869px; height: 510px; }
  .card-back  { left: 162px; top: 630px; width: 868px; height: 508px; }

  .band-light { position: absolute; left: 0; right: 0; top: 313px; height: 158px; background: var(--band-light); }
  .band-strong { position: absolute; left: 0; right: 0; top: 471px; bottom: 0; background: var(--band-strong); }

  .person { position: absolute; left: 48px; top: 48px; width: 200px; }
  .person-name {
    margin: 0;
    font: 700 40px/1 "Open Sans", sans-serif;
    color: var(--ink);
    letter-spacing: -0.5px;
    white-space: nowrap;
  }
  .person-role {
    margin: 6px 0 0;
    font: italic 400 21px/1 "Open Sans", sans-serif;
    color: var(--ink);
    text-align: right;
  }

  .brand-front {
    position: absolute;
    left: 515px; top: 218px;
    font: 700 58px/1 "Open Sans", sans-serif;
    color: var(--brand-grey);
    letter-spacing: -1px;
  }

  .address {
    position: absolute;
    left: 515px; top: 344px;
    margin: 0;
    font: 400 30px/36px "Bebas Neue", sans-serif;
    color: var(--ink);
    letter-spacing: 1.5px;
    font-style: normal;
  }

  .brand-back {
    position: absolute;
    left: 0; right: 0; top: 162px;
    text-align: center;
    font: 400 96px/1 "Jura", sans-serif;
    color: var(--brand-blue);
    letter-spacing: -1px;
  }
  .tagline {
    position: absolute;
    left: 0; right: 0; top: 288px;
    text-align: center;
    margin: 0;
    font: 300 31px/1 "Open Sans", sans-serif;
    color: var(--tagline);
    word-spacing: 12px;
  }
  .services { position: absolute; left: 296px; top: 344px; width: 280px; height: 56px; }
</style>
</head>
<body>
<main class="canvas">

  <section class="card card-front" aria-label="Front of business card">
    <div class="band-light"></div>
    <div class="band-strong"></div>
    <div class="person">
      <h1 class="person-name">Tom Haskins</h1>
      <p class="person-role">CEO</p>
    </div>
    <div class="brand-front">Qbrook718</div>
    <address class="address">
      2419 Pelkey Avenue<br>
      J7R-2B8, Montreal<br>
      Quebec
    </address>
  </section>

  <section class="card card-back" aria-label="Back of business card">
    <div class="brand-back">QBrook718</div>
    <p class="tagline">SYNC | SELL | SHIP</p>
    <svg class="services" viewBox="0 0 280 56" aria-label="Sync, sell and ship icons">
      <g class="icon-sync" transform="translate(26 28)">
        <circle r="26" fill="var(--icon)"/>
        <path d="M-14 -2 A14 14 0 0 1 11 -8" fill="none" stroke="#fff" stroke-width="5"/>
        <path d="M6 -14 L16 -9 L8 -1 Z" fill="#fff"/>
        <path d="M14 2 A14 14 0 0 1 -11 8" fill="none" stroke="#fff" stroke-width="5"/>
        <path d="M-6 14 L-16 9 L-8 1 Z" fill="#fff"/>
      </g>
      <g class="icon-sell" transform="translate(139 28)">
        <circle r="26" fill="var(--icon)"/>
        <text x="0" y="12" text-anchor="middle" font-family="Open Sans, sans-serif" font-weight="700" font-size="34" fill="#fff">$</text>
      </g>
      <g class="icon-ship" transform="translate(252 28)">
        <circle r="26" fill="var(--icon)"/>
        <path d="M-12 -10 H8 L15 -2 V8 H-12 Z" fill="#fff"/>
        <path d="M6 -7 L11 -2 H6 Z" fill="var(--icon)"/>
        <line x1="-20" y1="-6" x2="-14" y2="-6" stroke="#fff" stroke-width="2"/>
        <line x1="-20" y1="-1" x2="-14" y2="-1" stroke="#fff" stroke-width="2"/>
        <line x1="-20" y1="4" x2="-14" y2="4" stroke="#fff" stroke-width="2"/>
        <circle cx="-5" cy="9" r="4" fill="#fff" stroke="var(--icon)" stroke-width="2"/>
        <circle cx="8" cy="9" r="4" fill="#fff" stroke="var(--icon)" stroke-width="2"/>
      </g>
    </svg>
  </section>

</main>
</body>
</html>
```